Amber Ridge Partners Business Card

A business card design to accompany the logo design you completed on Pixel Forum. We are open to your proposals. I did add one idea below that might work, but we aren't married to the idea. The company is a real estate services company. Clientele are typically high net worth individuals, executive level employment or owners of their own company, 30-60 years old.

Our 1 (bad?) idea: double sided card; One side landscape with logo and word mark. Other side Portrait with the logo only (oversize watermark maybe?). Somewhere add text of Name (Marcus Tellingham), Title (Principal), phone # (555-214-7736) and email address (marcus@amberridgeco.example). There would be a second design with my wife's name, number and email in place of mine.

Again totally open to ideas here.

Industry/Entity Type

Real Estate

```html
<!DOCTYPE html>
<html lang="en">
<head>
<meta charset="utf-8">
<title>Amber Ridge Partners — Business Card Alternatives</title>
<link rel="stylesheet" href="https://fonts.googleapis.com/css2?family=Source+Sans+3:ital,wght@0,400;0,600;0,700;1,400&display=swap">
<style>
  :root {
    --sage: #639455;
    --ink: #111111;
    --muted: #6f6f6f;
    --rule: #8a8a8a;
    --paper: #ffffff;
  }
  * { margin: 0; padding: 0; box-sizing: border-box; }
  html, body {
    width: 1200px; height: 1000px; overflow: hidden;
    background: var(--paper);
    font-family: "Source Sans 3", "Myriad Pro", Arial, sans-serif;
    color: var(--ink);
  }
  .sheet { position: relative; width: 1200px; height: 1000px; }

  .card {
    position: absolute;
    border: 1px solid var(--rule);
    background: var(--paper);
    overflow: hidden;
  }
  .card--back-landscape  { left: 0; top: 0; width: 542px; height: 331px; }
  .card--front-landscape { left: 660px; top: 0; width: 540px; height: 331px; }
  .card--back-portrait   { left: 0; top: 460px; width: 332px; height: 540px; }
  .card--front-portrait  { left: 870px; top: 460px; width: 330px; height: 540px; }

  /* Oversize back-side disc with the company name */
  .back-disc {
    position: absolute; border-radius: 50%; background: var(--sage);
  }
  .card--back-landscape .back-disc { width: 1380px; height: 1380px; left: -419px; top: 22px; }
  .card--back-portrait .back-disc  { width: 1240px; height: 1240px; left: -454px; top: 48px; }
  .back-name {
    position: absolute; color: var(--paper); font-weight: 400; white-space: nowrap;
  }
  .card--back-landscape .back-name { left: 40px; top: 150px; font-size: 46px; }
  .card--back-portrait .back-name  { left: 30px; top: 250px; font-size: 46px; line-height: 54px; white-space: normal; width: 260px; }

  .divider {
    position: absolute; left: 0; width: 1200px; height: 0;
    border-top: 1px solid var(--rule);
  }
  .divider--upper { top: 330px; }
  .divider--lower { top: 460px; }
  .edge { position: absolute; right: 0; top: 330px; width: 0; height: 131px; border-right: 1px solid var(--rule); }

  .alt-label {
    position: absolute; left: 409px;
    font-weight: 700; font-size: 15px; letter-spacing: 20.5px;
    white-space: pre; color: var(--ink);
  }
  .alt-label--one { top: 350px; }
  .alt-label--two { top: 460px; }

  .brand {
    position: absolute; display: flex; align-items: center;
    color: var(--sage); font-weight: 400; white-space: nowrap;
  }
  .brand__dot { border-radius: 50%; background: var(--sage); flex: none; }
  .brand--landscape { left: 70px; top: 94px; font-size: 36px; gap: 18px; }
  .brand--landscape .brand__dot { width: 60px; height: 60px; }
  .brand--portrait { left: 30px; top: 141px; font-size: 22px; gap: 12px; }
  .brand--portrait .brand__dot { width: 44px; height: 44px; }

  .person { position: absolute; }
  .person__name { font-weight: 700; font-size: 18px; line-height: 22px; }
  .person__title { font-style: italic; font-size: 14px; color: var(--muted); line-height: 17px; }
  .contact { position: absolute; font-size: 15px; line-height: 22px; }
  .contact__label { font-size: 14px; color: var(--muted); }

  .card--front-landscape .person  { left: 221px; top: 198px; }
  .card--front-landscape .contact { left: 221px; top: 259px; }
  .card--front-portrait .person   { left: 60px; top: 273px; }
  .card--front-portrait .contact  { left: 60px; top: 378px; }
</style>
</head>
<body>
<main class="sheet">

  <section class="card card--back-landscape">
    <div class="back-disc"></div>
    <p class="back-name">Amber Ridge Partners</p>
  </section>

  <section class="card card--front-landscape">
    <div class="brand brand--landscape"><span class="brand__dot"></span>Amber Ridge Partners</div>
    <div class="person">
      <p class="person__name">Marcus Tellingham</p>
      <p class="person__title">Principal</p>
    </div>
    <div class="contact">
      <p><span class="contact__label">phone:</span> 555-214-7736</p>
      <p><span class="contact__label">email:</span> marcus@amberridgeco.example</p>
    </div>
  </section>

  <div class="divider divider--upper"></div>
  <div class="edge"></div>
  <p class="alt-label alt-label--one">ALTERNATIVE 1</p>
  <p class="alt-label alt-label--two">ALTERNATIVE 2</p>
  <div class="divider divider--lower"></div>

  <section class="card card--back-portrait">
    <div class="back-disc"></div>
    <p class="back-name">Amber Ridge Partners</p>
  </section>

  <section class="card card--front-portrait">
    <div class="brand brand--portrait"><span class="brand__dot"></span>Amber Ridge Partners</div>
    <div class="person">
      <p class="person__name">Marcus Tellingham</p>
      <p class="person__title">Principal</p>
    </div>
    <div class="contact">
      <p><span class="contact__label">phone:</span> 555-214-7736</p>
      <p><span class="contact__label">email:</span> marcus@amberridgeco.example</p>
    </div>
  </section>

</main>
</body>
</html>
```